Flyer für Tiertherapeutin
Eine sehr motivierte und kreative Designerin. Schon der erste Vorschlag war ganz nach meinen Vorstellungen.
Zielgruppe
Ich bin Tiertherapeutin für TCVM und Ernährungsberaterin für Hunde und Katzen. Mittels Akupunktur, Lasertherapie, Mykotherapie und Ernährungsberatung kommt es zu einer Linderung vorhandener Schmerzen, eine verbesserte Regulation der Organe und einer Steigerung das Wohlbefindens sowie Lebensqualität.
Zielgruppe sind überwiegend weibliche Hunde- und Katzenbesitzer mit erkrankten Tieren.
Aufgabenstellung
Flyer sollte klappbar sein. Logo und mein Name und Kontaktdaten sollten enthalten sein.

```html
<!DOCTYPE html>
<html lang="de">
<head>
<meta charset="utf-8">
<title>Tiertherapie – Flyer Innenseite</title>
<link href="https://fonts.googleapis.com/css2?family=Poppins:wght@400;700&display=swap" rel="stylesheet">
<style>
  :root {
    --panel: #d8efe3;
    --side-start: #edf7f1;
    --side-end: #f8fbf9;
    --ink: #23212f;
    --photo-sky: #9fb8d6;
    --photo-ground: #b39a7c;
    --photo-fur: #c98a4a;
  }
  * { margin: 0; padding: 0; box-sizing: border-box; }
  html, body { width: 1200px; height: 2545px; overflow: hidden; }
  body {
    position: relative;
    font-family: "Poppins", sans-serif;
    color: var(--ink);
    background: linear-gradient(90deg, var(--side-start), var(--side-end));
  }
  .panel {
    position: absolute; left: 0; top: 0;
    width: 1032px; height: 2545px;
    background: var(--panel);
  }
  .heading {
    position: absolute; left: 121px;
    font-weight: 700;
    font-size: 88px;
    line-height: 111px;
    letter-spacing: -0.5px;
  }
  .heading--benefits { top: 86px; }
  .heading--focus { top: 869px; }
  .heading--services { top: 1667px; }
  .intro {
    position: absolute; left: 121px; top: 330px;
    width: 880px;
    font-size: 38.5px;
    line-height: 55px;
  }
  .photo {
    position: absolute; left: 121px; top: 1136px;
    width: 911px; height: 486px;
    background: linear-gradient(180deg, var(--photo-sky) 0%, #d7dde2 28%, var(--photo-fur) 52%, var(--photo-ground) 70%, #9b8468 100%);
  }
  .services {
    position: absolute; left: 121px; top: 1918px;
    list-style: none;
    font-size: 38.5px;
    line-height: 55px;
  }
  .services li { position: relative; padding-left: 76px; width: 880px; }
  .services li::before {
    content: ""; position: absolute; left: 23px; top: 22px;
    width: 12px; height: 12px; border-radius: 50%;
    background: var(--ink);
  }
</style>
</head>
<body>
  <div class="panel"></div>

  <h2 class="heading heading--benefits">Vorteile<br>der Tiertherapie:</h2>

  <p class="intro">Mein Ziel ist es, den Körper deines<br>Tieres in ein inneres Gleichgewicht zu<br>bringen, die Selbstheilungskräfte zu<br>aktivieren und dies führt zu einem<br>schmerzfreien und gesunden Leben<br>deines besten Fellfreundes. Meine<br>Therapiemethoden lindern nicht nur<br>die Symptome, sondern lösen die<br>Ursachen auf.</p>

  <h2 class="heading heading--focus">Dein Tier<br>im Mittelpunkt!</h2>

  <div class="photo" role="img" aria-label="Foto: eine rot-weiße Katze und ein rotbrauner Hund liegen nebeneinander in der Sonne auf einem Hof"></div>

  <h2 class="heading heading--services">Leistungen im<br>Überblick:</h2>

  <ul class="services">
    <li>Katzenverhaltenstraining</li>
    <li>Ernährungsberatung für Hunde und Katzen</li>
    <li>Ganzheitliche Behandlung nach TCVM</li>
    <li>Akupunktur</li>
    <li>Laserbehandlung</li>
    <li>chinesische Kräuterheilkunde</li>
    <li>Mykotherapie</li>
    <li>Darmaufbau</li>
  </ul>
</body>
</html>
```